Brand design for Varundel Partners

We are a new start up Fund Manager based in Singapore in need of a stylish and slick corporate identity starting with letterhead and business card (2 separate projects on craft hive but must be completed as one). We are aiming to be a somewhat 'budget' service provider with a target market of high net worth individuals and savvy self traders so we need to have our look convey value but with style. Our logo is attached and the use of the blue is imperative. The company name is Varundel Partners Pte Ltd and the verbiage 'Licensed by the Financial Oversight Board of Singapore - RFMC licence no. QRT804217-3' should be incorporated in small print.

Business card should also include address, office, direct and mobile numbers as well as email address. Follow me on twitter/fb/linkedin/Google+ should also be incrorporated. We are also looking to have a QR code on the business card that people can read with a smartphone which will auto populate our contact details in to their address book.

Many thanks and happy designing!

Reason: Extending so we can have further internal discussions. Thanks for input so far, some great designs coming through! Cheers

```html
<!DOCTYPE html>
<html lang="en">
<head>
<meta charset="utf-8">
<title>Varundel Partners – Letterhead</title>
<link href="https://fonts.googleapis.com/css2?family=Carlito:wght@400;700&display=swap" rel="stylesheet">
<style>
  :root {
    --brand-blue: #0b4fa3;
    --band-blue: #0450a6;
    --faint-blue: #bfc6e6;
    --paper: #ffffff;
    --backdrop: #e9e9ec;
  }
  * { margin: 0; padding: 0; box-sizing: border-box; }
  html, body {
    width: 1009px;
    height: 1200px;
    overflow: hidden;
    background: var(--backdrop);
    font-family: "Carlito", "Calibri", sans-serif;
  }
  .letterhead {
    position: absolute;
    left: 80px;
    top: 0;
    width: 849px;
    height: 1200px;
    background: var(--paper);
    overflow: hidden;
  }
  .brand-name {
    position: absolute;
    left: 24px;
    top: 72px;
    font-size: 64px;
    font-weight: 400;
    letter-spacing: 1px;
    line-height: 1;
    color: var(--brand-blue);
  }
  .company-contact {
    position: absolute;
    left: 572px;
    top: 34px;
    color: var(--brand-blue);
    font-size: 18px;
    font-style: normal;
    line-height: 22px;
    white-space: nowrap;
  }
  .company-contact .company-title {
    font-size: 24px;
    line-height: 30px;
    margin-bottom: 2px;
  }
  .company-contact .contact-line {
    padding-left: 2px;
  }
  .decor-name {
    position: absolute;
    left: 380px;
    top: 560px;
    font-size: 430px;
    font-weight: 700;
    line-height: 1;
    color: var(--faint-blue);
    white-space: nowrap;
    user-select: none;
  }
  .licence-band {
    position: absolute;
    left: 0;
    bottom: 0;
    width: 100%;
    height: 40px;
    background: var(--band-blue);
    color: #fff;
    font-size: 15px;
    line-height: 40px;
    text-align: center;
  }
</style>
</head>
<body>
  <main class="letterhead">
    <div class="brand-name">VARUNDEL</div>

    <address class="company-contact">
      <div class="company-title">Varundel Partners Pte Ltd</div>
      <div class="contact-line">14 Tembusu Lane</div>
      <div class="contact-line">Singapore 248512</div>
      <div class="contact-line">P: +65 0000 4218</div>
      <div class="contact-line">E: contact@varundel.sg</div>
    </address>

    <div class="decor-name" aria-hidden="true">VA</div>

    <footer class="licence-band">
      Licensed by the Financial Oversight Board of Singapore - RFMC licence no. QRT804217-3
    </footer>
  </main>
</body>
</html>
```